Website Re-Design

We would like to explore the possibility of a re-design of our website. We want all the content that it currently has to remain on the pages, and we don't want our logo/corporate identity or colours changed, so it is literally just a website re-design.

Our website is www.trovalink.co.uk

Websites that we like are

http://www.quillmarsh.co.uk/
http://rankwidget.com/

```html
<!DOCTYPE html>
<html lang="en">
<head>
<meta charset="utf-8">
<title>Trovalink – Inbound Marketing &amp; SEO</title>
<link href="https://fonts.googleapis.com/css2?family=Open+Sans:wght@300;400;600;700&display=swap" rel="stylesheet">
<style>
:root{
  --pink:#e5007d;
  --green:#8cc63e;
  --teal:#1db3a6;
  --ink:#333;
  --muted:#666;
  --dark:#111;
  --white:#fff;
}
*{box-sizing:border-box;margin:0;padding:0}
html,body{width:1200px;height:3120px;overflow:hidden}
body{font-family:"Open Sans",Arial,sans-serif;color:var(--ink);background:var(--white);position:relative}
.site-nav{height:56px;display:flex;align-items:center;justify-content:space-between;padding:0 40px;background:var(--white)}
.brand{font-size:26px;font-weight:700;color:var(--pink);letter-spacing:1px}
.menu{display:flex;gap:26px;font-size:14px;color:var(--muted)}
.menu .active{color:var(--green)}
.hero{position:relative;height:624px}
.hero-photo{height:524px;background:linear-gradient(120deg,#c9d3da 0%,#8d9aa4 45%,#4e5a63 100%)}
.hero-strip{height:100px;background:var(--dark);display:flex;align-items:center;justify-content:space-between;padding:0 40px}
.hero-strip p{color:var(--white);font-size:30px;font-weight:300;white-space:nowrap}
.btn{display:inline-block;border-radius:30px;font-weight:600;text-transform:uppercase;letter-spacing:1px;white-space:nowrap}
.btn-pink{background:var(--pink);color:var(--white);padding:14px 46px;font-size:16px}
.intro{height:480px;display:flex;align-items:center;justify-content:space-between;padding:0 40px 0 40px}
.intro-text{width:620px}
.intro-brand{font-size:52px;font-weight:700;color:var(--pink);line-height:1}
.intro-tag{font-size:26px;font-weight:300;color:var(--ink);margin:8px 0 22px}
.intro-text p{font-size:15px;line-height:1.6;color:var(--muted);margin-bottom:14px}
.intro-art{width:400px;height:400px;margin-right:40px;border-radius:50%;background:radial-gradient(circle at 45% 45%,#eaf6ff 0%,#9cd3ef 45%,#6a7c8a 100%)}
.portfolio{height:600px;background:var(--green);padding:25px 40px;display:grid;grid-template-columns:repeat(4,1fr);grid-template-rows:repeat(3,170px);gap:20px}
.tile{background:var(--white);display:flex;flex-direction:column;padding:8px}
.tile-img{flex:1;background:linear-gradient(135deg,#f3b6d6,#9ed3c8)}
.tile-cap{font-size:13px;padding-top:6px;color:var(--ink);white-space:nowrap;overflow:hidden;text-overflow:ellipsis}
.tile-text{background:#2b2b2b;color:var(--white);padding:16px;font-size:13px;line-height:1.5}
.tile-text strong{display:block;font-size:14px;margin-bottom:6px}
.portfolio-title{grid-column:2 / span 2;background:var(--white);display:flex;align-items:center;justify-content:center;font-size:64px;font-weight:300;color:var(--pink);letter-spacing:2px}
.clients{height:520px;background:var(--teal);padding:28px 40px}
.clients h2{text-align:center;color:var(--white);font-size:28px;font-weight:400;margin-bottom:34px}
.client-grid{display:grid;grid-template-columns:repeat(6,1fr);grid-template-rows:repeat(3,120px);gap:16px}
.client{background:var(--white);display:flex;align-items:center;justify-content:center;font-size:18px;font-weight:600;color:var(--ink);white-space:nowrap}
.cta{height:280px;background:var(--pink);text-align:center;color:var(--white);padding-top:50px}
.cta h2{font-size:32px;font-weight:300;margin-bottom:14px}
.cta p{font-size:17px;width:760px;margin:0 auto 28px;line-height:1.5}
.btn-dark{background:var(--dark);color:var(--white);padding:16px 110px;font-size:28px;font-weight:400}
.location{position:relative;height:480px}
.map{position:absolute;inset:0;background:linear-gradient(135deg,#eceae5,#d9d6cf)}
.pin{position:absolute;left:600px;top:180px}
.contact-card{position:absolute;left:40px;top:120px;width:420px;background:var(--white);padding:30px;box-shadow:0 2px 10px rgba(0,0,0,.12)}
.contact-card .brand{font-size:30px;display:block;margin-bottom:20px}
.contact-row{display:flex;align-items:center;gap:12px;font-size:14px;color:var(--muted);margin-bottom:16px}
.dot{width:16px;height:16px;border-radius:50%;background:var(--teal);flex:none}
.site-footer{height:80px;display:flex;align-items:center;justify-content:space-between;padding:0 40px;font-size:14px;color:var(--muted);background:var(--white)}
.social{display:flex;gap:10px}
.social span{width:30px;height:30px;border-radius:50%;background:var(--teal)}
</style>
</head>
<body>
<header class="site-nav">
  <span class="brand">TROVALINK</span>
  <nav class="menu"><span class="active">Home</span><span>About Us</span><span>Portfolio</span><span>What We Do</span></nav>
</header>

<section class="hero">
  <div class="hero-photo" role="img" aria-label="Photo of a young team gathered around a laptop"></div>
  <div class="hero-strip">
    <p>Trovalink takes a holistic view of earning your customers attention</p>
    <span class="btn btn-pink">Talk to us</span>
  </div>
</section>

<section class="intro">
  <div class="intro-text">
    <div class="intro-brand">Trovalink</div>
    <div class="intro-tag">your inbound marketing &amp; SEO performance agency</div>
    <p>Do you want to earn your customers attention? Gain more visibility in the SERPs and build &amp; engage with your audience?</p>
    <p>Trovalink specialises in SEO, Social media, CRO and Design &amp; Creative services. Offering a bespoke and personal service from a team of digital natives.</p>
  </div>
  <div class="intro-art" role="img" aria-label="Illustration of circles showing a team, speech bubbles, SEO and social media"></div>
</section>

<section class="portfolio">
  <div class="tile-text"><strong>Branding &amp; PR, SEO, Social</strong>The best way to reach your audience through a great campaign, built to grow reach and engage readers today.</div>
  <div class="tile"><div class="tile-img" role="img" aria-label="Infographic preview"></div><div class="tile-cap">Infographics - Wayfarer Guide</div></div>
  <div class="tile"><div class="tile-img" role="img" aria-label="Video still preview"></div><div class="tile-cap">Palace Dance Challenge</div></div>
  <div class="tile"><div class="tile-img" role="img" aria-label="Social asset preview"></div><div class="tile-cap">Social Assets - Wayfarer Guide</div></div>
  <div class="tile"><div class="tile-img" role="img" aria-label="Social asset preview"></div><div class="tile-cap">Social Assets - Wayfarer Guide</div></div>
  <div class="portfolio-title">PORTFOLIO</div>
  <div class="tile"><div class="tile-img" role="img" aria-label="Infographic preview"></div><div class="tile-cap">Infographics - Wayfarer Guide</div></div>
  <div class="tile"><div class="tile-img" role="img" aria-label="Campaign preview"></div><div class="tile-cap">Best Mates Wish List</div></div>
  <div class="tile"><div class="tile-img" role="img" aria-label="Infographic preview"></div><div class="tile-cap">Infographics - Wayfarer Guide</div></div>
  <div class="tile"><div class="tile-img" role="img" aria-label="Video still preview"></div><div class="tile-cap">Palace Dance Challenge</div></div>
  <div class="tile"><div class="tile-img" role="img" aria-label="Social asset preview"></div><div class="tile-cap">Social Assets - Wayfarer Guide</div></div>
</section>

<section class="clients">
  <h2>OUR CLIENTS</h2>
  <div class="client-grid">
    <div class="client">Fieldmart</div><div class="client">CoachStream</div><div class="client">Wayfarer Guide</div><div class="client">Staymore</div><div class="client">Fieldmart</div><div class="client">CoachStream</div>
    <div class="client">Fieldmart</div><div class="client">CoachStream</div><div class="client">Wayfarer Guide</div><div class="client">Staymore</div><div class="client">CoachStream</div><div class="client">Wayfarer Guide</div>
    <div class="client">Fieldmart</div><div class="client">CoachStream</div><div class="client">Wayfarer Guide</div><div class="client">Staymore</div><div class="client">CoachStream</div><div class="client">Wayfarer Guide</div>
  </div>
</section>

<section class="cta">
  <h2>Interested in what you have seen so far?</h2>
  <p>Are you looking for a progressive and innovative inbound marketing agency who can work alongside your existing teams. If Yes, then let's have a chat.</p>
  <span class="btn btn-dark">CONTACT US</span>
</section>

<section class="location">
  <div class="map" role="img" aria-label="Street map of the office surroundings"></div>
  <svg class="pin" width="28" height="40" viewBox="0 0 28 40" aria-hidden="true"><path d="M14 0C6 0 0 6 0 14c0 10 14 26 14 26s14-16 14-26C28 6 22 0 14 0z" fill="#e5007d"/><circle cx="14" cy="14" r="5" fill="#fff"/></svg>
  <div class="contact-card">
    <span class="brand">TROVALINK</span>
    <div class="contact-row"><span class="dot"></span>14 Harlow Mews, Eastbridge, London, E9 4TQ</div>
    <div class="contact-row"><span class="dot"></span>Tel: +44 (0)20 7946 0321</div>
    <div class="contact-row"><span class="dot"></span>Email: hello@trovalink.co.uk</div>
  </div>
</section>

<footer class="site-footer">
  <span>© 2015 Trovalink, Inc. All rights reserved. Terms &amp; Privacy</span>
  <div class="social"><span></span><span></span><span></span><span></span><span></span><span></span><span></span><span></span></div>
</footer>
</body>
</html>
```